General Contractors need a new Crisp updated Card Design

We need a new business card design for our company of 25 years based in Toronto call Holvaster Building Inc. : Our goal is to be the leading commercial contractors in Toronto by providing exceptional value to our clients. We work very hard to deliver professional, quality, service in conjunction with consistent price competitiveness to all of our clients on every single project.

Target Market(s)

Design & Build Clients

Industry/Entity Type

Construction Company

Contact Information for Business Card

Address:
18 North Tamlin Glen Road, Unit 57, Marbrook Vale, ON, K7T 2R9
Office: 905-218-5937

Holvasters Logo
Employee Job Description
Employee Cell Phone #
Employee Email
www.holvaster-example.com

Colors

Designer to choose colors to be used in the design.

Requirements
Must have
• Quote Company Saying:
• "Professional. Quality. Service."
Nice to have
• New Crisp up to date look. simple & fresh ( Not to Busy)
Should not have
• NO BLUE PRINTS ON THE BUSINESS CARDS

```html
<!DOCTYPE html>
<html lang="en">
<head>
<meta charset="utf-8">
<title>Holvaster Building Inc. — Business Card</title>
<link rel="stylesheet" href="https://fonts.googleapis.com/css2?family=Libre+Baskerville:wght@400;700&display=swap">
<style>
  :root {
    --teal: #0b7d6f;
    --teal-dark: #05675b;
    --teal-light: #169a88;
    --ink: #3a3a3a;
    --paper: #ffffff;
    --bg: #e9ebea;
  }
  * { box-sizing: border-box; margin: 0; padding: 0; }
  html, body { width: 1200px; height: 1000px; overflow: hidden; background: var(--bg); }
  body { font-family: "Libre Baskerville", Georgia, serif; color: var(--ink); position: relative; }

  .card {
    position: absolute; left: 250px; width: 700px; height: 400px;
    box-shadow: 0 6px 18px rgba(0,0,0,.18);
    overflow: hidden;
  }
  .card-front { top: 60px; background: linear-gradient(135deg, var(--teal-light) 0%, var(--teal) 45%, var(--teal-dark) 100%); }
  .card-back { top: 530px; background: var(--paper); }

  .brand { display: flex; align-items: center; gap: 16px; }
  .brand-mark { width: 44px; height: 44px; flex: none; }
  .brand-name { font-weight: 700; font-size: 34px; letter-spacing: .5px; line-height: 1.1; white-space: nowrap; }
  .brand-line { display: block; }
  .card-front .brand { position: absolute; left: 50%; top: 50%; transform: translate(-50%, -50%); }
  .card-front .brand-mark { background: var(--paper); }
  .card-front .brand-name { color: var(--paper); }

  .card-back .brand { position: absolute; left: 48px; top: 128px; gap: 12px; }
  .card-back .brand-mark { background: var(--teal); width: 32px; height: 32px; }
  .card-back .brand-name { color: var(--teal); font-size: 22px; }

  .person { position: absolute; right: 44px; top: 40px; text-align: right; }
  .person-name { font-weight: 700; font-size: 22px; color: var(--teal); letter-spacing: 1px; }
  .person-title { font-size: 14px; color: var(--ink); margin-top: 6px; }

  .rule { position: absolute; height: 1.5px; background: var(--teal); }
  .rule-top { left: 330px; right: 44px; top: 106px; }
  .rule-top::after { content: ""; position: absolute; right: 30px; top: -4px; width: 8px; height: 8px; background: var(--teal); }
  .rule-mid { left: 30px; right: 30px; top: 250px; }

  .details { list-style: none; position: absolute; font-size: 14px; line-height: 1.55; }
  .details li { display: flex; align-items: flex-start; gap: 10px; }
  .details svg { width: 15px; height: 15px; flex: none; margin-top: 3px; fill: var(--teal); }
  .details-web { left: 340px; top: 124px; width: 316px; }
  .details-contact { left: 30px; top: 266px; }

  .tagline {
    position: absolute; left: 30px; right: 30px; bottom: 36px;
    font-size: 17px; letter-spacing: 7px; color: var(--ink);
    display: flex; align-items: center; gap: 12px;
  }
  .tagline .dot { width: 8px; height: 8px; background: var(--teal); display: inline-block; }
  .band { position: absolute; left: 0; right: 0; bottom: 0; height: 20px; background: var(--teal); }
</style>
</head>
<body>
  <section class="card card-front" aria-label="Card front">
    <div class="brand">
      <span class="brand-mark"></span>
      <span class="brand-name"><span class="brand-line">HOLVASTER</span><span class="brand-line">BUILDING INC.</span></span>
    </div>
  </section>

  <section class="card card-back" aria-label="Card back">
    <div class="brand">
      <span class="brand-mark"></span>
      <span class="brand-name"><span class="brand-line">HOLVASTER</span><span class="brand-line">BUILDING INC.</span></span>
    </div>

    <div class="person">
      <div class="person-name">DORIAN KESSEL</div>
      <div class="person-title">President</div>
    </div>
    <div class="rule rule-top"></div>

    <ul class="details details-web">
      <li>
        <svg viewBox="0 0 16 16"><circle cx="8" cy="8" r="7"/><path d="M1 8h14M8 1c3 3 3 11 0 14M8 1c-3 3-3 11 0 14" stroke="#fff" stroke-width="1" fill="none"/></svg>
        <span>www.holvaster-example.com</span>
      </li>
      <li>
        <svg viewBox="0 0 16 16"><path d="M8 0a5.5 5.5 0 0 0-5.5 5.5C2.5 10 8 16 8 16s5.5-6 5.5-10.5A5.5 5.5 0 0 0 8 0z"/><circle cx="8" cy="5.5" r="2" fill="#fff"/></svg>
        <span>18 North Tamlin Glen Road, Unit 57<br>Marbrook Vale, ON, K7T 2R9</span>
      </li>
    </ul>

    <div class="rule rule-mid"></div>

    <ul class="details details-contact">
      <li>
        <svg viewBox="0 0 16 16"><path d="M3 1l3 3-1.5 2a9 9 0 0 0 5.5 5.5L12 10l3 3-2 2C6 15 1 10 1 3z"/></svg>
        <span>416-309-7781</span>
      </li>
      <li>
        <svg viewBox="0 0 16 16"><rect x="4" y="1" width="8" height="5"/><rect x="1" y="6" width="14" height="6" rx="1"/><rect x="4" y="10" width="8" height="5" fill="#fff" stroke="#0b7d6f"/></svg>
        <span>905-218-6640</span>
      </li>
      <li>
        <svg viewBox="0 0 16 16"><rect x="1" y="3" width="14" height="10"/><path d="M1 3l7 6 7-6" stroke="#fff" stroke-width="1.2" fill="none"/></svg>
        <span>dk@holvaster-example.com</span>
      </li>
    </ul>

    <p class="tagline">PROFESSIONAL <span class="dot"></span> QUALITY <span class="dot"></span> SERVICE</p>
    <div class="band"></div>
  </section>
</body>
</html>
```